Design a Journal (Cover + Page) for Print

Looking to create a beautiful design for daily personal journal in Adobe InDesign.

Notebook cover dimensions is 8.5" inches x 11" inches

I have the interior page template and sections as I want (Attached). I need you to design it in InDesign.

As far as the exterior cover, I want something clean. I have attached a cover I like for your inspiration and give you an idea what i mean by "Clean"

Your design of the Cover and interior pages needs to be coherent.

```html
<!DOCTYPE html>
<html lang="en">
<head>
<meta charset="utf-8">
<title>Journal 2020 Cover</title>
<link href="https://fonts.googleapis.com/css2?family=Jost:wght@300;400&display=swap" rel="stylesheet">
<style>
  :root {
    --ocean-deep: #1f7fcf;
    --ocean-mid: #3aa6e3;
    --ocean-light: #8fd0f0;
    --ocean-pale: #b9e2f5;
    --label-white: #ffffff;
    --label-gold: #f2b544;
    --title-blue: #3ea2d8;
  }

  html, body {
    margin: 0;
    padding: 0;
    width: 848px;
    height: 1200px;
    overflow: hidden;
    background: #ffffff;
  }

  .journal-cover {
    position: relative;
    width: 848px;
    height: 1200px;
    overflow: hidden;
  }

  .cover-texture {
    position: absolute;
    inset: 0;
    background:
      radial-gradient(ellipse 38% 30% at 38% 62%, var(--ocean-pale) 0%, rgba(185,226,245,0) 100%),
      radial-gradient(ellipse 30% 22% at 70% 30%, rgba(143,208,240,0.9) 0%, rgba(143,208,240,0) 100%),
      radial-gradient(ellipse 25% 40% at 95% 50%, rgba(185,226,245,0.8) 0%, rgba(185,226,245,0) 100%),
      radial-gradient(ellipse 35% 45% at 0% 10%, var(--ocean-deep) 0%, rgba(31,127,207,0) 100%),
      radial-gradient(ellipse 30% 40% at 0% 95%, var(--ocean-deep) 0%, rgba(31,127,207,0) 100%),
      radial-gradient(ellipse 30% 30% at 80% 75%, rgba(31,127,207,0.7) 0%, rgba(31,127,207,0) 100%),
      linear-gradient(160deg, var(--ocean-mid) 0%, var(--ocean-light) 55%, var(--ocean-mid) 100%);
  }

  .cover-label {
    position: absolute;
    left: 210px;
    top: 158px;
    width: 427px;
    height: 152px;
    box-sizing: border-box;
    background: var(--label-white);
    border: 6px solid var(--label-gold);
    text-align: center;
    font-family: "Jost", "Futura", sans-serif;
    color: var(--title-blue);
  }

  .cover-title {
    margin: 0;
    padding-top: 14px;
    font-weight: 300;
    font-size: 64px;
    line-height: 72px;
    letter-spacing: 2px;
  }

  .cover-year {
    margin: 2px 0 0;
    font-weight: 400;
    font-size: 27px;
    line-height: 32px;
    letter-spacing: 1px;
  }
</style>
</head>
<body>
  <main class="journal-cover">
    <div class="cover-texture" role="img" aria-label="Blue watercolour wash texture with a glossy foil sheen"></div>
    <div class="cover-label">
      <h1 class="cover-title">JOURNAL</h1>
      <p class="cover-year">2020</p>
    </div>
  </main>
</body>
</html>
```